Tender Lantern Letterhead Design Project

We need a letterhead design for a consultancy business based in Australia.

Tender Lantern is a unique business designed to assist with the complex and time consuming nature of selecting contractors, showing them what to do and reviewing quotes when it comes to body corporate and strata maintenance items such as painting, waterproofing, plumbing and electrical.

Target Market(s)

apartment managers

Industry/Entity Type

Business

Requirements
Must have
• must have logo and contact details

Tender Lantern
82 Corvalla Ridge Road
Tarrowin, QLD 4871
Ph 07 5391 2846
Fax 07 5392 8071
Mobile 0438 917204

```html
<!DOCTYPE html>
<html lang="en">
<head>
<meta charset="utf-8">
<title>Tender Lantern Letterhead</title>
<link rel="stylesheet" href="https://fonts.googleapis.com/css2?family=Arimo:wght@400;700&display=swap">
<style>
  :root {
    --backdrop: #d9d9d9;
    --paper: #ffffff;
    --orange: #f39323;
    --red: #e52b2b;
    --grey: #c4c4c4;
    --name-grey: #8a8a8a;
    --ink: #1c1c1c;
    --footer-ink: #6d6d6d;
  }
  * { margin: 0; padding: 0; box-sizing: border-box; }
  html, body {
    width: 1200px; height: 900px; overflow: hidden;
    background: var(--backdrop);
    font-family: "Arimo", Arial, sans-serif;
  }
  .letterhead {
    position: absolute; left: 290px; top: 12px;
    width: 620px; height: 877px;
    background: var(--paper);
    box-shadow: 0 2px 10px rgba(0,0,0,0.18);
    overflow: hidden;
  }
  .letterhead__art { position: absolute; inset: 0; }
  .brand-name {
    position: absolute; right: 22px; top: 44px;
    font-size: 20px; font-weight: 700; color: var(--name-grey);
    letter-spacing: 0.3px; line-height: 1; white-space: nowrap;
  }
  .letter {
    position: absolute; left: 31px; top: 80px; width: 478px;
    font-size: 9.6px; line-height: 1.9; color: var(--ink);
  }
  .letter__meta {
    display: flex; gap: 112px; font-weight: 700; margin-bottom: 18px;
  }
  .letter__salutation { font-weight: 700; margin-bottom: 14px; }
  .letter p { margin-bottom: 16px; }
  .letter__signoff { line-height: 1.9; }
  .contact {
    position: absolute; left: 31px; top: 808px;
    font-size: 8.6px; color: var(--footer-ink); letter-spacing: 0.1px;
  }
</style>
</head>
<body>
  <main class="letterhead">
    <svg class="letterhead__art" width="620" height="877" viewBox="0 0 620 877" aria-hidden="true">
      <path class="header-sweep" d="M236,0 H620 V34 C520,34 370,26 236,0 Z" fill="var(--orange)"/>
      <rect class="footer-band footer-band--orange" x="0" y="735" width="360" height="26" fill="var(--orange)"/>
      <rect class="footer-band footer-band--grey" x="424" y="735" width="196" height="26" fill="var(--grey)"/>
      <rect class="footer-band footer-band--grey-low" x="210" y="765" width="410" height="20" fill="var(--grey)"/>
      <rect class="footer-square" x="352" y="722" width="72" height="58" fill="var(--red)" stroke="#ffffff" stroke-width="2"/>
    </svg>

    <div class="brand-name">Tender Lantern</div>

    <article class="letter">
      <div class="letter__meta">
        <span>Water Plumbing - Regent Road</span>
        <span>22/09/2011</span>
      </div>
      <div class="letter__salutation">Dear Customer,</div>
      <p>Lorem ipsum dolor sit amet, consectetur adipiscing elit. Donec elementum velit sit amet libero fringilla adipiscing. Aliquam sollicitudin, leo vitae molestie facilisis, tellus ligula varius velit, vitae tincidunt lacus purus vitae nulla. Nulla imperdiet, odio quis ultrices ornare, diam est dictum lacus, et vehicula est magna et metus. Integer mattis lorem quis tortor accumsan ultrices ac ut massa. Duis eget metus ut risus scelerisque ornare quis eget dui. Aliquam lobortis dolor vitae magna volutpat eu facilisis tellus molestie. Sed a purus quis nibh lacinia interdum ut at leo. Sed sem dui, mollis in pellentesque sed, placerat non erat. Cum sociis natoque penatibus et magnis dis parturient montes, nascetur ridiculus mus. In lacinia arcu non felis laoreet sed convallis lectus tincidunt. Duis quis mauris et enim egestas molestie vel id sem.</p>
      <p>Integer consequat velit quis elit hendrerit imperdiet. Donec felis velit, volutpat vel convallis nec, sollicitudin et nulla. Pellentesque sodales elementum aliquam. Donec convallis, turpis sit amet laoreet ultricies, enim est elementum magna, dictum lobortis eros tellus quis diam. Nunc suscipit augue non nisl volutpat volutpat. Ut egestas ultrices purus, eget varius nibh placerat in. Cras leo ante, congue id ultricies a, ornare eu est. Curabitur eleifend tincidunt mi eget tristique.</p>
      <p>Etiam arcu augue, ornare vitae consectetur luctus, tincidunt vitae urna. Lorem ipsum dolor sit amet, consectetur adipiscing elit. Donec vitae tortor quis orci adipiscing lobortis. Morbi aliquet orci quis mi viverra sollicitudin. Sed eget pellentesque turpis. Aliquam commodo sodales ultrices. Nullam ut elit vitae elit suscipit porttitor viverra non mi. Donec diam mi, tincidunt nec sodales vestibulum, iaculis a urna. Nulla facilisi. Integer consequat velit quis elit hendrerit imperdiet. Donec felis velit, volutpat vel convallis nec, sollicitudin et nulla. Pellentesque sodales elementum aliquam. Donec convallis, turpis sit amet laoreet ultricies.</p>
      <div class="letter__signoff">Thanking you,<br>Myself</div>
    </article>

    <footer class="contact">Tender Lantern | 82 Corvalla Ridge Road | Tarrowin, QLD 4871 | Ph 07 5391 2846 | Fax 07 5392 8071 | Mobile 0438 917204</footer>
  </main>
</body>
</html>
```